Strategic design partner needed for newly global technical consultancy! Starting with PowerPoint!

Quillforte.biz is a new consulting company offering technical assurance (reliability, business and cyber resiliency, operational excellence, and technical agility). We already have a logo (attached) and main font (Montserrat). Our colour scheme is gold and charcoal (color code of charcoal is #36454F, and for the gold is #B69904).
See the attachment for full colour palette we want! We need to partner with a designer for our corporate branding, starting with a PowerPoint deck that will be used for proposals and client meetings.
In a proposal deck we have items like Problem Statement (our joint understanding), Our Approach, Architecture, Timeline, Team, Assumptions/Dependencies/Risks, RACI, Pricing.
For corporate presentations we would have Introduction, Services, Methodology, Case Studies, Team, Clients, Contact.
This could lead to much more work. The website is just a placeholder, but we like the colours (quillforte dot biz)

Industry/Entity Type

Technology solutions apply across all industries. We have clients in fintech, pharma, retail, etc.

Requirements
Must have
• Match the colour scheme - SEE UPLOADED ATTACHMENT

```html
<!DOCTYPE html>
<html lang="en">
<head>
<meta charset="utf-8">
<title>Quillforte Timeline Slides</title>
<link href="https://fonts.googleapis.com/css2?family=Montserrat:wght@400;500;600;700&display=swap" rel="stylesheet">
<style>
  :root {
    --charcoal: #36454F;
    --gold: #B69904;
    --gold-line: #cdb75a;
    --slide-light: #e8e8e8;
    --slide-dark: #dcdcdc;
    --page: #fdfdfd;
    --text: #4a4f55;
    --rule: #c9c9c9;
  }
  html, body {
    margin: 0;
    padding: 0;
    width: 1200px;
    height: 1200px;
    overflow: hidden;
    background: var(--page);
    font-family: "Montserrat", sans-serif;
  }
  .slide {
    position: absolute;
    top: 56px;
    width: 537px;
    height: 302px;
  }
  .slide--timeline-one { left: 44px; }
  .slide--timeline-two { left: 626px; }
  .slide svg { display: block; width: 100%; height: 100%; }
  .slide-title { font-family: "Montserrat", sans-serif; font-size: 34px; font-weight: 400; fill: var(--charcoal); }
  .note { font-family: "Montserrat", sans-serif; font-size: 9.3px; fill: var(--text); }
  .step-number { font-family: "Montserrat", sans-serif; font-size: 11px; font-weight: 700; fill: #fff; }
  .year { font-family: "Montserrat", sans-serif; font-size: 16px; font-weight: 700; fill: var(--gold); }
  .footer-text { font-family: "Montserrat", sans-serif; font-size: 7px; fill: var(--charcoal); }
  .brand-name { font-family: "Montserrat", sans-serif; font-size: 10.5px; font-weight: 600; fill: var(--charcoal); }
</style>
</head>
<body>

<section class="slide slide--timeline-one">
  <svg viewBox="0 0 859 483" xmlns="http://www.w3.org/2000/svg">
    <defs>
      <linearGradient id="slideBgOne" x1="0" y1="1" x2="1" y2="0">
        <stop offset="0" stop-color="var(--slide-light)"/>
        <stop offset="0.5" stop-color="#e9e9e9"/>
        <stop offset="1" stop-color="var(--slide-dark)"/>
      </linearGradient>
    </defs>
    <rect class="slide-bg" width="859" height="483" fill="url(#slideBgOne)"/>
    <rect class="side-band side-band--charcoal" x="0" y="0" width="14" height="242" fill="var(--charcoal)"/>
    <rect class="side-band side-band--gold" x="0" y="242" width="14" height="241" fill="var(--gold)"/>
    <text class="slide-title" x="45" y="60">Timeline 1</text>

    <path class="route" fill="none" stroke="var(--gold-line)" stroke-width="1"
      d="M51,117 H505 A26,26 0 0 1 531,143 A26,26 0 0 1 505,169 H418 A26.5,26.5 0 0 0 392,195.5 A26.5,26.5 0 0 0 418,222 H773 A26.5,26.5 0 0 1 799.5,248.5 A26.5,26.5 0 0 1 773,275 H153 A26,26 0 0 0 127,301 A26,26 0 0 0 153,327 H419 A27,27 0 0 1 445,354 A27,27 0 0 1 419,381 H271 A26,26 0 0 0 245,407 A26,26 0 0 0 271,433 H734"/>

    <g class="steps">
      <g><circle cx="97" cy="117" r="11.5" fill="var(--gold)"/><text class="step-number" x="97" y="121" text-anchor="middle">1</text></g>
      <g><circle cx="246" cy="117" r="11.5" fill="var(--gold)"/><text class="step-number" x="246" y="121" text-anchor="middle">2</text></g>
      <g><circle cx="482" cy="116" r="11.5" fill="var(--gold)"/><text class="step-number" x="482" y="120" text-anchor="middle">3</text></g>
      <g><circle cx="392" cy="196" r="11.5" fill="var(--gold)"/><text class="step-number" x="392" y="200" text-anchor="middle">4</text></g>
      <g><circle cx="549" cy="222" r="11.5" fill="var(--gold)"/><text class="step-number" x="549" y="226" text-anchor="middle">5</text></g>
      <g><circle cx="738" cy="222" r="11.5" fill="var(--gold)"/><text class="step-number" x="738" y="226" text-anchor="middle">6</text></g>
      <g><circle cx="738" cy="275" r="11.5" fill="var(--gold)"/><text class="step-number" x="738" y="279" text-anchor="middle">7</text></g>
      <g><circle cx="593" cy="275" r="11.5" fill="var(--gold)"/><text class="step-number" x="593" y="279" text-anchor="middle">8</text></g>
      <g><circle cx="198" cy="275" r="11.5" fill="var(--gold)"/><text class="step-number" x="198" y="279" text-anchor="middle">9</text></g>
      <g><circle cx="172" cy="327" r="11.5" fill="var(--gold)"/><text class="step-number" x="172" y="331" text-anchor="middle">9</text></g>
      <g><circle cx="445" cy="353" r="11.5" fill="var(--gold)"/><text class="step-number" x="445" y="357" text-anchor="middle">10</text></g>
      <g><circle cx="620" cy="434" r="11.5" fill="var(--gold)"/><text class="step-number" x="620" y="438" text-anchor="middle">11</text></g>
    </g>

    <g class="notes">
      <text class="note" text-anchor="middle"><tspan x="97" y="142">Lorem ipsum dolor sit</tspan><tspan x="97" y="154">amet, consectetur</tspan><tspan x="97" y="166">adipiscing elit</tspan></text>
      <text class="note" text-anchor="middle"><tspan x="246" y="142">Lorem ipsum dolor sit</tspan><tspan x="246" y="154">amet, consectetur</tspan><tspan x="246" y="166">adipiscing elit</tspan></text>
      <text class="note" text-anchor="middle"><tspan x="482" y="74">Lorem ipsum dolor sit</tspan><tspan x="482" y="86">amet, consectetur</tspan><tspan x="482" y="98">adipiscing elit</tspan></text>
      <text class="note" text-anchor="end"><tspan x="374" y="196">Lorem ipsum dolor sit</tspan><tspan x="374" y="208">amet, consectetur</tspan><tspan x="374" y="220">adipiscing elit</tspan></text>
      <text class="note" text-anchor="middle"><tspan x="546" y="183">Lorem ipsum dolor sit</tspan><tspan x="546" y="195">amet, consectetur</tspan><tspan x="546" y="207">adipiscing elit</tspan></text>
      <text class="note" text-anchor="middle"><tspan x="735" y="183">Lorem ipsum dolor sit</tspan><tspan x="735" y="195">amet, consectetur</tspan><tspan x="735" y="207">adipiscing elit</tspan></text>
      <text class="note" text-anchor="middle"><tspan x="202" y="232">Lorem ipsum dolor sit</tspan><tspan x="202" y="244">amet, consectetur</tspan><tspan x="202" y="256">adipiscing elit</tspan></text>
      <text class="note" text-anchor="middle"><tspan x="591" y="298">Lorem ipsum dolor sit</tspan><tspan x="591" y="310">amet, consectetur</tspan><tspan x="591" y="322">adipiscing elit</tspan></text>
      <text class="note" text-anchor="middle"><tspan x="735" y="298">Lorem ipsum dolor sit</tspan><tspan x="735" y="310">amet, consectetur</tspan><tspan x="735" y="322">adipiscing elit</tspan></text>
      <text class="note" text-anchor="middle"><tspan x="171" y="354">Lorem ipsum dolor sit</tspan><tspan x="171" y="366">amet, consectetur</tspan><tspan x="171" y="378">adipiscing elit</tspan></text>
      <text class="note" text-anchor="start"><tspan x="459" y="349">Lorem ipsum dolor sit</tspan><tspan x="459" y="361">amet, consectetur</tspan><tspan x="459" y="373">adipiscing elit</tspan></text>
      <text class="note" text-anchor="middle"><tspan x="620" y="394">Lorem ipsum dolor sit</tspan><tspan x="620" y="406">amet, consectetur</tspan><tspan x="620" y="418">adipiscing elit</tspan></text>
    </g>

    <line class="footer-rule" x1="45" y1="461" x2="753" y2="461" stroke="var(--gold-line)" stroke-width="0.6"/>
    <text class="footer-text" x="45" y="470">Presentation Title  |  2</text>
    <rect class="brand-mark" x="793" y="447" width="12" height="12" fill="var(--gold)"/>
    <text class="brand-name" x="799" y="477" text-anchor="middle">QUILLFORTE</text>
  </svg>
</section>

<section class="slide slide--timeline-two">
  <svg viewBox="0 0 859 483" xmlns="http://www.w3.org/2000/svg">
    <defs>
      <linearGradient id="slideBgTwo" x1="0" y1="1" x2="1" y2="0">
        <stop offset="0" stop-color="var(--slide-light)"/>
        <stop offset="0.5" stop-color="#e9e9e9"/>
        <stop offset="1" stop-color="var(--slide-dark)"/>
      </linearGradient>
    </defs>
    <rect class="slide-bg" width="859" height="483" fill="url(#slideBgTwo)"/>
    <rect class="side-band side-band--charcoal" x="0" y="0" width="14" height="242" fill="var(--charcoal)"/>
    <rect class="side-band side-band--gold" x="0" y="242" width="14" height="241" fill="var(--gold)"/>
    <text class="slide-title" x="45" y="60">Timeline 2</text>

    <line class="axis" x1="51" y1="241" x2="816" y2="241" stroke="var(--rule)" stroke-width="0.8"/>
    <path class="axis-arrow" d="M817,238 L823,241 L817,244 Z" fill="var(--gold)"/>

    <g class="milestones" fill="var(--gold)" stroke="#f2f2f2" stroke-width="2">
      <circle cx="86" cy="241" r="6.5"/>
      <circle cx="172" cy="241" r="6.5"/>
      <circle cx="258" cy="241" r="6.5"/>
      <circle cx="345" cy="241" r="6.5"/>
      <circle cx="431" cy="241" r="6.5"/>
      <circle cx="517" cy="241" r="6.5"/>
      <circle cx="603" cy="241" r="6.5"/>
      <circle cx="689" cy="241" r="6.5"/>
      <circle cx="775" cy="241" r="6.5"/>
    </g>

    <g class="years" text-anchor="middle">
      <text class="year" x="86" y="220">2018</text>
      <text class="year" x="258" y="220">2020</text>
      <text class="year" x="431" y="220">2022</text>
      <text class="year" x="603" y="220">2024</text>
      <text class="year" x="775" y="220">2026</text>
      <text class="year" x="172" y="279">2019</text>
      <text class="year" x="345" y="279">2021</text>
      <text class="year" x="517" y="279">2023</text>
      <text class="year" x="689" y="279">2025</text>
    </g>

    <g class="notes" text-anchor="middle">
      <text class="note"><tspan x="86" y="167">Lorem ipsum dolor sit</tspan><tspan x="86" y="179">amet, consectetur</tspan><tspan x="86" y="191">adipiscing elit</tspan></text>
      <text class="note"><tspan x="258" y="167">Lorem ipsum dolor sit</tspan><tspan x="258" y="179">amet, consectetur</tspan><tspan x="258" y="191">adipiscing elit</tspan></text>
      <text class="note"><tspan x="431" y="167">Lorem ipsum dolor sit</tspan><tspan x="431" y="179">amet, consectetur</tspan><tspan x="431" y="191">adipiscing elit</tspan></text>
      <text class="note"><tspan x="603" y="167">Lorem ipsum dolor sit</tspan><tspan x="603" y="179">amet, consectetur</tspan><tspan x="603" y="191">adipiscing elit</tspan></text>
      <text class="note"><tspan x="775" y="167">Lorem ipsum dolor sit</tspan><tspan x="775" y="179">amet, consectetur</tspan><tspan x="775" y="191">adipiscing elit</tspan></text>
      <text class="note"><tspan x="172" y="305">Lorem ipsum dolor sit</tspan><tspan x="172" y="317">amet, consectetur</tspan><tspan x="172" y="329">adipiscing elit</tspan></text>
      <text class="note"><tspan x="345" y="305">Lorem ipsum dolor sit</tspan><tspan x="345" y="317">amet, consectetur</tspan><tspan x="345" y="329">adipiscing elit</tspan></text>
      <text class="note"><tspan x="517" y="305">Lorem ipsum dolor sit</tspan><tspan x="517" y="317">amet, consectetur</tspan><tspan x="517" y="329">adipiscing elit</tspan></text>
      <text class="note"><tspan x="689" y="305">Lorem ipsum dolor sit</tspan><tspan x="689" y="317">amet, consectetur</tspan><tspan x="689" y="329">adipiscing elit</tspan></text>
    </g>

    <line class="footer-rule" x1="45" y1="461" x2="753" y2="461" stroke="var(--gold-line)" stroke-width="0.6"/>
    <text class="footer-text" x="45" y="470">Presentation Title  |  2</text>
    <rect class="brand-mark" x="793" y="447" width="12" height="12" fill="var(--gold)"/>
    <text class="brand-name" x="799" y="477" text-anchor="middle">QUILLFORTE</text>
  </svg>
</section>

</body>
</html>
```